Hi,
We are an accounting firm looking to upgrade the following:
Logo, letterhead, withcomp slips and maybe our business cards. I have attached our original letterhead (sample A) and a letterhead (SAmple B) which we like the design and layout, however I want to stick with the colours of our orginal letterhead (Sample A) but improve and modernise the look with other letter head (Sample B) I have attached both. On the footer of Sample A, we would like to remove the names of the directors but leave EST. 1985 we also want to add the QRT logo ABN and TAX AGENT logo as stated in Sample B , we would like to do a layout for the header similar to SAmple B however maybe a bit more structured.

```html
<!DOCTYPE html>
<html lang="en">
<head>
<meta charset="utf-8">
<title>Brentholm Accountants – Stationery</title>
<link rel="stylesheet" href="https://fonts.googleapis.com/css2?family=Montserrat:wght@600;700&family=Arimo:wght@400;700&display=swap">
<style>
:root{
  --stage:#3a3b3d;
  --paper:#f6f3f3;
  --card:#ffffff;
  --navy:#163d78;
  --band:#124a8f;
  --ink:#3b3b3b;
  --muted:#555;
  --body-text:#5a5a5a;
  --bar-1:#e2e1e3;
  --bar-2:#e0e3ea;
  --bar-3:#dde6f2;
  --badge-a:#d9d9de;
  --badge-b:#cfd6c8;
}
*{margin:0;padding:0;box-sizing:border-box}
html,body{width:1200px;height:793px;overflow:hidden;background:var(--stage);font-family:'Arimo',Arial,sans-serif;color:var(--ink)}
.canvas{position:relative;width:1200px;height:793px}
.sheet{position:absolute;overflow:hidden}
.band{position:absolute;left:0;right:0;bottom:0;background:var(--band)}

.wordmark{font-family:'Montserrat',Arial,sans-serif;font-weight:600;color:var(--navy);line-height:1;white-space:nowrap}
.wordmark .name{display:block;letter-spacing:-0.2px}
.wordmark .sub{display:flex;align-items:center;gap:.35em;justify-content:flex-end}
.wordmark .sub i{display:inline-block;width:.62em;height:.62em;background:currentColor}

.icon{width:7px;height:7px;fill:var(--navy);vertical-align:-1px;margin-right:3px}
.contact-line{white-space:nowrap}

/* business card front */
.card-front{left:162px;top:55px;width:340px;height:193px;background:var(--card);border-radius:10px}
.card-front .band{height:11px}
.card-front .wordmark{position:absolute;right:184px;top:79px;text-align:right}
.card-front .wordmark .name{font-size:19px}
.card-front .wordmark .sub{font-size:10.5px;margin-top:3px}
.card-front .divider{position:absolute;left:168px;top:48px;width:1px;height:102px;background:var(--navy)}
.card-front .details{position:absolute;left:178px;top:44px;font-size:7.6px;line-height:9.8px;color:#333}
.card-front .person{font-family:'Arimo',sans-serif;font-weight:700;font-size:12.5px;color:var(--navy);line-height:14px}
.card-front .role{color:var(--muted);margin-bottom:6px}
.card-front .address{margin-bottom:5px}

/* business card back */
.card-back{left:155px;top:276px;width:346px;height:198px;background:var(--band);border-radius:10px}
.card-back .wordmark{position:absolute;left:0;right:0;top:66px;color:#fff;text-align:center}
.card-back .wordmark .name{font-size:36px}
.card-back .wordmark .sub{font-size:19px;justify-content:center;margin-top:4px}
.card-back .est{position:absolute;left:0;right:0;top:171px;text-align:center;font-size:7.6px;color:#fff}

/* compliment slip */
.comp-slip{left:62px;top:502px;width:536px;height:243px;background:var(--paper)}
.comp-slip .band{height:11px}
.comp-slip .wordmark{position:absolute;left:28px;top:28px;text-align:left}
.comp-slip .wordmark .name{font-size:21px}
.comp-slip .wordmark .sub{font-size:11.5px;margin-top:4px}
.comp-slip .title{position:absolute;right:21px;top:24px;font-family:'Montserrat',sans-serif;font-weight:700;font-size:23px;color:var(--navy)}
.bar{position:absolute}
.bar.one{background:var(--bar-1)}
.bar.two{background:var(--bar-2)}
.bar.three{background:var(--bar-3)}
.comp-slip .bar{width:66px;bottom:11px}
.comp-slip .contacts{position:absolute;left:28px;top:184px;font-size:7.6px;line-height:11.3px;color:#333}
.comp-slip .est{position:absolute;left:293px;top:208px;font-size:7.6px;color:#444}
.badge-plain{position:absolute;background:var(--badge-a);border-radius:3px}
.badge-round{position:absolute;border-radius:50%;background:var(--badge-b);border:2px solid #444}

/* letterhead */
.letterhead{left:651px;top:69px;width:476px;height:671px;background:var(--paper)}
.letterhead .band{height:13px}
.letterhead .bar{bottom:13px;width:98px}
.letterhead .wordmark{position:absolute;left:47px;top:52px;text-align:left}
.letterhead .wordmark .name{font-size:20px}
.letterhead .wordmark .sub{font-size:11px;margin-top:4px}
.letterhead .contacts{position:absolute;right:45px;top:56px;text-align:right;font-size:7.4px;line-height:11.2px;color:#333}
.letter{position:absolute;left:47px;top:163px;width:383px}
.salutation{font-size:13px;color:#444;margin-bottom:24px}
.letter p{font-size:7.2px;line-height:11.4px;color:var(--body-text);text-align:justify;margin-bottom:11.5px}
.sign-off{position:absolute;left:47px;top:456px;font-size:7.4px;color:#444}
.signature{position:absolute;left:47px;top:470px;width:60px;height:14px;background:#cfcfd3;border-radius:7px}
.signer{position:absolute;left:50px;top:508px;font-size:10.5px;color:#444;line-height:13px}
.signer small{display:block;font-size:8px;color:#555}
.letterhead .footer-note{position:absolute;left:44px;top:631px;font-size:7.6px;color:#444;word-spacing:1px}
.letterhead .footer-note span{margin-right:8px}
</style>
</head>
<body>
<svg width="0" height="0" style="position:absolute" aria-hidden="true">
  <symbol id="i-pin" viewBox="0 0 10 10"><path d="M5 0a3.6 3.6 0 0 0-3.6 3.6C1.4 6.3 5 10 5 10s3.6-3.7 3.6-6.4A3.6 3.6 0 0 0 5 0zm0 5a1.4 1.4 0 1 1 0-2.8A1.4 1.4 0 0 1 5 5z"/></symbol>
  <symbol id="i-phone" viewBox="0 0 10 10"><path d="M2.2 0.6l1.6 1.8-.9 1.3c.6 1.3 1.6 2.3 2.9 2.9l1.3-.9 1.8 1.6-.9 1.7C4.6 9 1 5.4.5 1.5z"/></symbol>
  <symbol id="i-fax" viewBox="0 0 10 10"><path d="M2.5 0h5v3h-5zM0 3.5h10v4.5H8V10H2V8H0zm3 3.5v2h4V7z"/></symbol>
  <symbol id="i-mail" viewBox="0 0 10 10"><path d="M0 2h10v6H0zm1 1l4 2.8L9 3z" fill-rule="evenodd"/></symbol>
  <symbol id="i-globe" viewBox="0 0 10 10"><circle cx="5" cy="5" r="5"/></symbol>
</svg>

<main class="canvas">

  <section class="sheet card-front" aria-label="Business card, front">
    <div class="wordmark"><span class="name">Brentholm</span><span class="sub"><i></i>Accountants</span></div>
    <div class="divider"></div>
    <div class="details">
      <div class="person">Owen Hartley</div>
      <div class="role">President</div>
      <div class="address">Brentholm Pty Ltd<br>418 Ridge Road<br>Ashdale Vic. 3190</div>
      <div class="contact-line"><svg class="icon"><use href="#i-phone"/></svg>+61 3 9000 4172</div>
      <div class="contact-line"><svg class="icon"><use href="#i-fax"/></svg>+61 3 9000 4173</div>
      <div class="contact-line"><svg class="icon"><use href="#i-mail"/></svg>info@brentholm.com.au</div>
      <div class="contact-line"><svg class="icon"><use href="#i-globe"/></svg>brentholmaccountants.com.au</div>
    </div>
    <div class="band"></div>
  </section>

  <section class="sheet card-back" aria-label="Business card, back">
    <div class="wordmark"><span class="name">Brentholm</span><span class="sub"><i></i>Accountants</span></div>
    <div class="est">EST. 1985</div>
  </section>

  <section class="sheet comp-slip" aria-label="Compliment slip">
    <div class="bar one" style="left:274px;height:116px"></div>
    <div class="bar two" style="left:368px;height:143px"></div>
    <div class="bar three" style="left:461px;height:170px"></div>
    <div class="wordmark"><span class="name">Brentholm</span><span class="sub"><i></i>Accountants</span></div>
    <h1 class="title">With Compliments</h1>
    <div class="contacts">
      <div class="contact-line"><svg class="icon"><use href="#i-pin"/></svg>Brentholm Pty Ltd, 418 Ridge Road, Ashdale Vic. 3190</div>
      <div class="contact-line"><svg class="icon"><use href="#i-phone"/></svg>+61 3 9000 4172 &nbsp;<svg class="icon"><use href="#i-fax"/></svg>+61 3 9000 4173</div>
      <div class="contact-line"><svg class="icon"><use href="#i-mail"/></svg>info@brentholm.com.au &nbsp;<svg class="icon"><use href="#i-globe"/></svg>www.brentholmaccountants.com.au</div>
    </div>
    <div class="est">EST. 1985</div>
    <div class="badge-plain" role="img" aria-label="Professional body badge" style="left:402px;top:192px;width:60px;height:32px"></div>
    <div class="badge-round" role="img" aria-label="Registered tax agent badge" style="left:478px;top:192px;width:34px;height:34px"></div>
    <div class="band"></div>
  </section>

  <section class="sheet letterhead" aria-label="Letterhead">
    <div class="bar one" style="left:51px;top:494px"></div>
    <div class="bar two" style="left:190px;top:454px"></div>
    <div class="bar three" style="left:327px;top:418px"></div>
    <div class="wordmark"><span class="name">Brentholm</span><span class="sub"><i></i>Accountants</span></div>
    <div class="contacts">
      <div class="contact-line"><svg class="icon"><use href="#i-pin"/></svg>Brentholm Pty Ltd, 418 Ridge Road, Ashdale Vic. 3190</div>
      <div class="contact-line"><svg class="icon"><use href="#i-phone"/></svg>+61 3 9000 4172 <svg class="icon"><use href="#i-fax"/></svg>+61 3 9000 4173</div>
      <div class="contact-line"><svg class="icon"><use href="#i-mail"/></svg>info@brentholm.com.au <svg class="icon"><use href="#i-globe"/></svg>www.brentholmaccountants.com.au</div>
    </div>
    <article class="letter">
      <div class="salutation">Dear Mr. Carver,</div>
      <p>Lorem ipsum dolor sit amet, consectetur adipiscing elit. Donec orci purus, luctus vitae dignissim eu, iaculis sed purus. Vivamus faucibus, ipsum nec aliquet viverra, leo mauris condimentum ligula, sit amet sagittis enim ligula quis arcu. Nam egestas tortor id nisi porttitor mattis. In tortor ante, ultricies in suscipit a, tempus non massa. Vivamus et auctor mi. Fusce vel massa nulla. Phasellus nec eros mauris, et scelerisque orci.</p>
      <p>Donec malesuada orci vitae nulla accumsan porta a id massa. Quisque accumsan iaculis magna sit amet fringilla. Maecenas consequat, magna eget tincidunt semper, odio nibh rutrum mi, id feugiat ante nisi eu risus. Vestibulum nunc orci, rhoncus a placerat in, ultricies in mi. Cras mattis varius eros, vel fringilla nisi suscipit eget. Quisque scelerisque sagittis nulla at porttitor.</p>
      <p>Sed id augue vitae urna euismod commodo aliquet a quam. Pellentesque arcu velit, cursus et malesuada ut, consequat et diam. Nullam erat sem, rhoncus id ullamcorper vitae, rhoncus et arcu. In ultricies ultricies nulla, ut rutrum nisi iaculis at. Donec eu magna a metus ornare faucibus. Fusce aliquet faucibus ultricies. Morbi semper, est id tincidunt gravida, sem arcu adipiscing lacus, ac bibendum nulla leo eu purus. Quisque nec diam sed risus consectetur a ccumsan quis quis nibh. Vestibulum id purus lorem.</p>
      <p>It is a long established fact that a reader will be distracted by the readable content of a page when looking at its layout. The point of using Lorem Ipsum is that it has a more-or-less normal distribution of letters, as opposed to using 'Content here, content here', making it look like readable English. Many desktop publishing packages</p>
    </article>
    <div class="sign-off">Sincerely,</div>
    <div class="signature" role="img" aria-label="Handwritten signature"></div>
    <div class="signer">Martin Carver<small>CEO/ Founder</small></div>
    <div class="footer-note"><span>EST. 1985</span>ABN 00 123 456 789</div>
    <div class="badge-plain" role="img" aria-label="Professional body badge" style="left:312px;top:604px;width:60px;height:34px"></div>
    <div class="badge-round" role="img" aria-label="Registered tax agent badge" style="left:401px;top:604px;width:42px;height:42px"></div>
    <div class="band"></div>
  </section>

</main>
</body>
</html>
```